postcard for Real Estate Agent that sells homes for less than any other agents

My company sells houses for a fraction of what others charge. I have most of the verbiage but I am open to ideas.
Our post card will be 6.25 x 9
We need an image that goes with our words and draws people to take a look
We are playful at the same time very serious about the money we will save our clients. In the past our message has been received as too good to be true. Our old message was "save $6000* when you list with us" We think the "*" was causing people to think their was a catch. Other agents will tell people that we will not do what they will do and that is why they must charge more. We are a full service agency and we will generally do everything that other agents will do and in many cases we will do more than other agents. We are changing this industry and need our message to get to every person that is thinking of selling their home

Target Market(s)

People who want to list their home for sale

Industry/Entity Type

Real Estate Agent

Requirements
Must have
• Image that makes people read the message

```html
<!DOCTYPE html>
<html lang="en">
<head>
<meta charset="utf-8">
<title>Postcard – Full Service Agency at a Fraction of the Cost</title>
<link rel="stylesheet" href="https://fonts.googleapis.com/css2?family=Montserrat:wght@700&family=Oswald:wght@700&family=Roboto+Condensed:wght@400;600&family=Jost:wght@400;500&display=swap">
<style>
  :root{
    --backdrop:#2a2a2a;
    --card:#ffffff;
    --blue:#1b8fcf;
    --blue-light:#8fd3f2;
    --navy:#1f3e5c;
    --ink:#2b2b2b;
    --green:#7fdc1f;
    --green-dark:#5a9e2a;
    --panel-top:#d6eef9;
    --panel-bottom:#ffffff;
  }
  *{margin:0;padding:0;box-sizing:border-box}
  html,body{width:900px;height:1200px;overflow:hidden;background:var(--backdrop)}
  .canvas{position:relative;width:900px;height:1200px}

  /* ---------- front side ---------- */
  .front{position:absolute;left:45px;top:22px;width:810px;height:562px;background:var(--card);overflow:hidden}
  .front svg{position:absolute;left:0;top:0}
  .front-copy{position:absolute;left:0;top:0;width:810px;text-align:center}
  .lead{position:absolute;top:246px;width:100%;font:700 34px/1 'Montserrat',sans-serif;color:var(--ink)}
  .shout{position:absolute;top:300px;width:100%;font:700 60px/1 'Oswald',sans-serif;color:var(--green);
         text-shadow:2px 3px 3px rgba(0,0,0,.45);letter-spacing:.5px}
  .claim{position:absolute;top:380px;width:100%;font:600 29px/1 'Roboto Condensed',sans-serif;color:var(--ink)}
  .offer{position:absolute;top:425px;width:100%;font:600 40px/1 'Roboto Condensed',sans-serif;color:var(--blue)}
  .uses{position:absolute;top:484px;width:100%;font:400 31px/1 'Roboto Condensed',sans-serif;color:var(--navy);
        display:flex;justify-content:center;align-items:center;gap:22px}
  .uses .sep{width:1px;height:26px;background:#a8c96a}

  /* ---------- back side ---------- */
  .back{position:absolute;left:45px;top:617px;width:810px;height:561px;background:var(--card);overflow:hidden}
  .message-panel{position:absolute;left:0;top:0;width:477px;height:561px;
                 background:linear-gradient(180deg,var(--panel-top),var(--panel-bottom))}
  .stamp-box{position:absolute;left:690px;top:30px;width:89px;height:98px;border:1px solid #333}
  .benefits{position:absolute;left:40px;top:32px;list-style:none;font:400 23px/32.5px 'Jost',sans-serif;color:var(--ink)}
  .benefits li{display:flex;align-items:center;gap:9px}
  .benefits svg{flex:none}
  .promise{position:absolute;left:0;top:278px;width:465px;height:100px;background:var(--blue);
           box-shadow:4px 6px 8px rgba(0,0,0,.3);color:#fff;font:400 31px/41px 'Jost',sans-serif;padding:11px 0 0 38px}
  .contact{position:absolute;left:40px;top:400px;font:400 27px/1 'Jost',sans-serif;color:var(--ink)}
  .contact-line{position:absolute;left:38px;display:flex;align-items:center;gap:10px;font:500 29px/1 'Jost',sans-serif;color:var(--ink)}
  .contact-line.phone{top:444px}
  .contact-line.web{top:485px;font-size:27px}
  .brand{position:absolute;left:610px;top:470px;width:180px;text-align:center}
  .brand-name{font:500 22px/1 'Jost',sans-serif;color:var(--navy)}
  .brand-phone{margin-top:12px;font:500 16px/1 'Jost',sans-serif;color:var(--green-dark)}
</style>
</head>
<body>
<div class="canvas">

  <section class="front">
    <svg width="810" height="562" viewBox="0 0 810 562">
      <defs>
        <linearGradient id="houseTones" x1="0" y1="0" x2="0" y2="1">
          <stop offset="0" stop-color="#a9cdea"/>
          <stop offset=".35" stop-color="#8e6a5a"/>
          <stop offset=".7" stop-color="#9a5a48"/>
          <stop offset="1" stop-color="#6f7a55"/>
        </linearGradient>
      </defs>
      <rect width="810" height="330" fill="url(#houseTones)" role="img" aria-label="Photo of a red brick two-storey house with trees and blue sky"/>
      <rect x="38" y="220" width="734" height="95" fill="rgba(235,235,235,.55)"/>
      <path d="M0,238 Q405,392 810,238 L810,252 Q405,404 0,252 Z" fill="var(--blue-light)"/>
      <path d="M0,252 Q405,404 810,252 L810,562 L0,562 Z" fill="var(--card)"/>
      <path d="M30,272 L30,525 Q30,537 42,537 L768,537 Q780,537 780,525 L780,272"
            fill="none" stroke="var(--blue)" stroke-width="7"/>
      <path d="M30,272 Q405,408 780,272" fill="none" stroke="var(--blue)" stroke-width="7"/>
      <rect x="38" y="220" width="734" height="95" fill="rgba(235,235,235,.35)"/>
    </svg>
    <div class="front-copy">
      <p class="lead">You’d have to be</p>
      <p class="shout">Bat $#@T CRAZY</p>
      <p class="claim">to give an agent $6000.00 To put a sign in your yard.</p>
      <p class="offer">Look at what you can do with $6000.00</p>
      <p class="uses"><span>Give it to your Kids</span><span class="sep"></span><span>Build a fence</span><span class="sep"></span><span>Build a deck</span></p>
    </div>
  </section>

  <section class="back">
    <div class="message-panel"></div>
    <div class="stamp-box"></div>

    <ul class="benefits">
      <li><svg width="17" height="17" viewBox="0 0 20 20"><circle cx="10" cy="10" r="8.5" fill="none" stroke="var(--blue)" stroke-width="1.6"/><path d="M6 10.2l2.8 2.8L14.5 7" fill="none" stroke="var(--blue)" stroke-width="1.8"/></svg>Landscape</li>
      <li><svg width="17" height="17" viewBox="0 0 20 20"><circle cx="10" cy="10" r="8.5" fill="none" stroke="var(--blue)" stroke-width="1.6"/><path d="M6 10.2l2.8 2.8L14.5 7" fill="none" stroke="var(--blue)" stroke-width="1.8"/></svg>Take a Vacation</li>
      <li><svg width="17" height="17" viewBox="0 0 20 20"><circle cx="10" cy="10" r="8.5" fill="none" stroke="var(--blue)" stroke-width="1.6"/><path d="M6 10.2l2.8 2.8L14.5 7" fill="none" stroke="var(--blue)" stroke-width="1.8"/></svg>Buy new clothes</li>
      <li><svg width="17" height="17" viewBox="0 0 20 20"><circle cx="10" cy="10" r="8.5" fill="none" stroke="var(--blue)" stroke-width="1.6"/><path d="M6 10.2l2.8 2.8L14.5 7" fill="none" stroke="var(--blue)" stroke-width="1.8"/></svg>Pay off your car</li>
      <li><svg width="17" height="17" viewBox="0 0 20 20"><circle cx="10" cy="10" r="8.5" fill="none" stroke="var(--blue)" stroke-width="1.6"/><path d="M6 10.2l2.8 2.8L14.5 7" fill="none" stroke="var(--blue)" stroke-width="1.8"/></svg>Pay off student loan</li>
      <li><svg width="17" height="17" viewBox="0 0 20 20"><circle cx="10" cy="10" r="8.5" fill="none" stroke="var(--blue)" stroke-width="1.6"/><path d="M6 10.2l2.8 2.8L14.5 7" fill="none" stroke="var(--blue)" stroke-width="1.8"/></svg>Buy New Carpet</li>
      <li><svg width="17" height="17" viewBox="0 0 20 20"><circle cx="10" cy="10" r="8.5" fill="none" stroke="var(--blue)" stroke-width="1.6"/><path d="M6 10.2l2.8 2.8L14.5 7" fill="none" stroke="var(--blue)" stroke-width="1.8"/></svg>Upgrade Appliances</li>
    </ul>

    <div class="promise">Full Service Agency at a<br>Fraction of the Cost</div>

    <p class="contact">Call Dale or Marcus</p>
    <p class="contact-line phone">
      <svg width="26" height="26" viewBox="0 0 26 26"><circle cx="13" cy="13" r="11.5" fill="none" stroke="var(--blue)" stroke-width="1.8"/><path d="M9 7.5c-1 .8-1.4 2-.9 3.4 1.1 3 3.3 5.4 6.2 6.6 1.4.6 2.6.2 3.4-.8l-2.2-2-1.3.9c-1.5-.7-2.7-1.9-3.4-3.4l.9-1.3z" fill="var(--blue)"/></svg>
      555.201.4437
    </p>
    <p class="contact-line web">
      <svg width="26" height="26" viewBox="0 0 26 26" fill="none" stroke="var(--blue)" stroke-width="1.8"><circle cx="13" cy="13" r="11"/><ellipse cx="13" cy="13" rx="5" ry="11"/><path d="M2 13h22M4 7h18M4 19h18"/></svg>
      www.HomeKeyRealty.com
    </p>

    <div class="brand">
      <p class="brand-name">Keystone Realty</p>
      <p class="brand-phone">555-310-0288</p>
    </div>
  </section>

</div>
</body>
</html>
```